Need full color yard sign designed

I need a catchy yard sign to attract people whom drive by to go to the website www.brickleafestimates.net to get a free no obligation value of their home. I like to use the location icon as part of the design. The design must be in both spanish and english top and bottom split design. I have attached the template format that the printing company needs me to use. I also need it in eps format. Also the sign will be double sided so same sign will be on both sidesPlease let me know if you have any questions about the design

Target Market(s)

Home owners looking to sell

Industry/Entity Type

Real Estate

Font styles to use
Sans Serif

Colors
f68d4d
fbed22
9bcb3b
0692cd

Requirements
Must have
• call to action theme. light colors since this is a sign and must also be seen at night
Nice to have
• colorful
Should not have
• dark background, too busy

```html
<!DOCTYPE html>
<html lang="en">
<head>
<meta charset="utf-8">
<title>Brickleaf Estimates Yard Sign</title>
<link rel="stylesheet" href="https://fonts.googleapis.com/css2?family=Cabin:wght@700&display=swap">
<style>
  :root {
    --sign-yellow: #fbed22;
    --sign-orange: #f68d4d;
    --sign-green: #9bcb3b;
    --sign-blue: #0692cd;
    --sign-white: #ffffff;
  }
  html, body {
    margin: 0;
    padding: 0;
    width: 1200px;
    height: 900px;
    overflow: hidden;
    background: var(--sign-white);
  }
  .yard-sign {
    position: relative;
    width: 1200px;
    height: 900px;
    background: var(--sign-white);
    font-family: "Cabin", "Gill Sans", sans-serif;
    font-weight: 700;
  }
  .band {
    position: absolute;
    left: 0;
    width: 1200px;
  }
  .band--yellow { background: var(--sign-yellow); }
  .band--headline {
    background: var(--sign-orange);
    color: var(--sign-white);
    display: flex;
    flex-direction: column;
    justify-content: center;
    align-items: center;
    text-align: center;
  }
  .band--url {
    background: var(--sign-white);
    display: flex;
    justify-content: center;
    align-items: center;
    gap: 18px;
  }
  .headline {
    margin: 0;
    font-size: 88px;
    line-height: 104px;
    letter-spacing: 1.5px;
    white-space: nowrap;
  }
  .headline--es {
    font-size: 74px;
    line-height: 96px;
    letter-spacing: 0.5px;
  }
  .location-pin {
    width: 54px;
    height: 72px;
    flex: none;
  }
  .location-pin__body { fill: var(--sign-green); }
  .location-pin__dot { fill: var(--sign-white); }
  .site-url {
    margin: 0;
    color: var(--sign-blue);
    font-size: 76px;
    letter-spacing: 1px;
    white-space: nowrap;
  }
  .top-edge    { top: 0;     height: 45px; }
  .english     { top: 45px;  height: 237px; }
  .english-url { top: 282px; height: 98px; }
  .mid-edge    { top: 380px; height: 45px; }
  .spanish     { top: 450px; height: 302px; }
  .spanish-url { top: 752px; height: 103px; }
  .bottom-edge { top: 855px; height: 45px; }
</style>
</head>
<body>
  <div class="yard-sign">
    <div class="band band--yellow top-edge"></div>

    <section class="band band--headline english" lang="en">
      <h1 class="headline">Get a FREE No Obligation<br>Home Market Evaluation</h1>
    </section>
    <div class="band band--url english-url">
      <svg class="location-pin" viewBox="0 0 24 32" aria-hidden="true">
        <path class="location-pin__body" d="M12 0C5.4 0 0 5.4 0 12c0 9 12 20 12 20s12-11 12-20C24 5.4 18.6 0 12 0z"/>
        <circle class="location-pin__dot" cx="12" cy="12" r="5"/>
      </svg>
      <p class="site-url">www.brickleafestimates.net</p>
    </div>

    <div class="band band--yellow mid-edge"></div>

    <section class="band band--headline spanish" lang="es">
      <h2 class="headline headline--es">Obtenga una Evaluación GRATIS<br>del Valor de su Casa<br>Sin Compromiso</h2>
    </section>
    <div class="band band--url spanish-url">
      <svg class="location-pin" viewBox="0 0 24 32" aria-hidden="true">
        <path class="location-pin__body" d="M12 0C5.4 0 0 5.4 0 12c0 9 12 20 12 20s12-11 12-20C24 5.4 18.6 0 12 0z"/>
        <circle class="location-pin__dot" cx="12" cy="12" r="5"/>
      </svg>
      <p class="site-url">www.brickleafestimates.net</p>
    </div>

    <div class="band band--yellow bottom-edge"></div>
  </div>
</body>
</html>
```